Redesign our Product Box!

We have a product box for our pet supplement we are looking to redesign. Please use the photoshop file of the current design for the logo/info/dieline and the concept picture of a bag we would like to see included in the box design.

Ideally the background will be the green with white text, but we really want it to be fun and appealing to pet owners so do not be scared to show your vision.

```html
<!DOCTYPE html>
<html lang="en">
<head>
<meta charset="utf-8">
<title>MarinaPaws Supplement Box Dieline</title>
<link href="https://fonts.googleapis.com/css2?family=Baloo+2:wght@500;700&family=Montserrat:wght@400;500;600&family=Oswald:wght@400;500&display=swap" rel="stylesheet">
<style>
  :root {
    --red: #a32a2b;
    --black: #111111;
    --peach: #f5ad7a;
    --peach-light: #fbe0cb;
    --green: #12a047;
    --ink: #222222;
    --white: #ffffff;
    --line: #1a1a1a;
  }
  * { margin: 0; padding: 0; box-sizing: border-box; }
  html, body { width: 1200px; height: 675px; overflow: hidden; background: var(--white); }
  body { position: relative; font-family: "Montserrat", sans-serif; color: var(--ink); }

  .dieline { position: absolute; left: 330px; top: 14px; width: 692px; height: 830px; transform: scale(0.78); transform-origin: 0 0; }
  .panel { position: absolute; overflow: hidden; background: var(--white); }
  .cut-lines { position: absolute; left: 0; top: 0; width: 692px; height: 830px; pointer-events: none; }

  .brand { font-family: "Baloo 2", sans-serif; font-weight: 700; color: var(--green); font-size: 21px; line-height: 1; letter-spacing: -0.3px; }
  .brand-dot { display: inline-block; width: 9px; height: 9px; border-radius: 50%; background: var(--red); margin-left: 4px; vertical-align: middle; }

  /* front */
  .front { left: 45px; top: 200px; width: 180px; height: 325px; }
  .front .brand { position: absolute; left: 16px; top: 25px; }
  .corner-peach { position: absolute; width: 54px; height: 54px; border-radius: 50%; background: var(--peach); }
  .front .corner-peach { right: -27px; top: -27px; }
  .side-arc { position: absolute; left: -35px; top: 110px; width: 70px; height: 70px; border-radius: 50%; background: var(--red); }
  .pet-art { position: absolute; left: 22px; top: 58px; width: 120px; height: 105px; border-radius: 10px; background: linear-gradient(135deg, #f7c39c, #f5ad7a 55%, #5a2a22); opacity: .9; }
  .front-title { position: absolute; left: 0; width: 100%; top: 175px; text-align: center; font-family: "Baloo 2", sans-serif; font-weight: 700; font-size: 12.5px; line-height: 1.15; color: var(--red); }
  .benefit { position: absolute; left: 23px; top: 213px; width: 134px; height: 36px; background: var(--red); color: var(--white); font-size: 10px; line-height: 1.15; text-align: center; padding-top: 4px; border-bottom: 3px solid var(--peach); }
  .front-mark { position: absolute; left: 68px; top: 256px; width: 42px; height: 42px; border-radius: 50%; border: 4px solid var(--red); background: var(--peach-light); }
  .audience { position: absolute; left: 55px; top: 305px; font-size: 9px; color: var(--red); }
  .audience b { font-weight: 600; }
  .net-weight { position: absolute; right: 12px; top: 302px; font-family: "Baloo 2", sans-serif; font-weight: 700; font-size: 13px; color: var(--red); }

  /* lid */
  .lid { left: 45px; top: 55px; width: 180px; height: 145px; background: transparent; }
  .lid-inner { position: absolute; inset: 0; transform: rotate(180deg); }
  .lid .brand { position: absolute; left: 16px; top: 42px; }
  .lid-mark { position: absolute; left: 69px; top: 78px; width: 40px; height: 40px; border-radius: 50%; border: 4px solid var(--red); background: var(--peach-light); }
  .lid-audience { position: absolute; left: 0; width: 100%; top: 125px; text-align: center; font-size: 8px; color: var(--red); }

  /* directions */
  .directions { left: 225px; top: 200px; width: 145px; height: 328px; }
  .directions .corner-peach { left: -27px; top: -27px; }
  .copy { font-size: 8px; line-height: 1.28; text-align: center; }
  .directions .dose { position: absolute; left: 14px; right: 8px; top: 22px; }
  .directions h2 { position: absolute; left: 0; right: 0; top: 86px; font-weight: 500; font-size: 11.5px; line-height: 1.2; text-align: center; color: var(--black); }
  .directions .story { position: absolute; left: 18px; right: 14px; top: 122px; }
  .directions .story p + p { margin-top: 9px; }
  .stripes { position: absolute; left: 0; right: 0; bottom: 0; }
  .stripes span { display: block; }
  .stripe-light { height: 8px; background: var(--peach-light); }
  .stripe-peach { height: 15px; background: var(--peach); }
  .stripe-red { height: 12px; background: var(--red); }

  /* facts */
  .print-side { position: absolute; left: 370px; top: 135px; width: 180px; text-align: center; font-weight: 600; font-size: 23px; line-height: 1.15; color: var(--black); }
  .facts { left: 370px; top: 200px; width: 180px; height: 328px; }
  .facts .corner-red { position: absolute; right: -28px; top: -28px; width: 56px; height: 56px; border-radius: 50%; background: var(--red); }
  .facts-table { position: absolute; left: 12px; top: 27px; width: 156px; font-family: "Oswald", sans-serif; }
  .facts-head { background: var(--red); color: var(--white); font-size: 17px; line-height: 1; padding: 6px 0 7px 14px; letter-spacing: 0.2px; }
  .facts-row { font-size: 6px; line-height: 1.3; padding: 2px 4px; display: flex; justify-content: space-between; }
  .row-peach { background: var(--peach); padding: 5px 4px; }
  .row-light { background: var(--peach-light); }
  .row-pale { background: #fdf0e5; }
  .facts .notice { position: absolute; left: 16px; right: 16px; top: 126px; font-size: 5.6px; line-height: 1.3; }
  .facts .distributor { position: absolute; left: 0; right: 0; top: 173px; font-size: 7.5px; line-height: 1.25; }
  .facts .warnings { position: absolute; left: 14px; right: 14px; top: 233px; font-size: 5.6px; line-height: 1.3; }
  .facts .care { position: absolute; left: 0; right: 0; top: 302px; font-size: 7.5px; line-height: 1.25; }

  /* back */
  .back { left: 550px; top: 193px; width: 142px; height: 335px; }
  .back-hero { position: absolute; left: -40px; top: 0; width: 222px; height: 115px; background: var(--red); border-radius: 0 0 111px 111px / 0 0 90px 90px; box-shadow: 0 4px 0 var(--peach); }
  .back-hero p { position: absolute; left: 56px; right: 56px; top: 31px; color: var(--white); font-size: 7.6px; line-height: 1.3; text-align: center; }
  .back .story { position: absolute; left: 12px; right: 10px; top: 124px; }
  .back .story p + p { margin-top: 8px; }

  /* bottom tuck */
  .lot-line { position: absolute; left: 370px; top: 636px; width: 180px; text-align: center; font-size: 7px; transform: rotate(180deg); }

  .swatches { position: absolute; left: 4px; top: 788px; display: flex; gap: 13px; }
  .swatch { width: 42px; height: 42px; }
  .swatch-red { background: var(--red); }
  .swatch-black { background: var(--black); }
  .swatch-peach { background: var(--peach); }
  .swatch-green { background: var(--green); }
</style>
</head>
<body>
<main class="dieline">

  <section class="panel lid" aria-label="Top lid">
    <div class="lid-inner">
      <div class="brand">MarinaPaws</div>
      <div class="lid-mark"></div>
      <div class="lid-audience">For Dogs &amp; Cats</div>
    </div>
  </section>

  <section class="panel front" aria-label="Front panel">
    <div class="corner-peach"></div>
    <div class="side-arc"></div>
    <div class="brand">MarinaPaws</div>
    <div class="pet-art" role="img" aria-label="Illustrated pet face with a star-shaped patch"></div>
    <h1 class="front-title">100% Pure Marine<br>Phytoplankton Powder</h1>
    <div class="benefit">Foundational Nutrition<br>&amp; Super-Antioxidant</div>
    <div class="front-mark"></div>
    <div class="audience">For <b>Dogs</b> &amp; <b>Cats</b></div>
    <div class="net-weight">15g</div>
  </section>

  <section class="panel directions" aria-label="Directions panel">
    <div class="corner-peach"></div>
    <p class="copy dose">Directions: For dogs &amp; cats 1/16tsp once per day. Administer orally. To be mixed into food. 1/16tsp = 1/2 the included scoop.</p>
    <h2>Unlock Nature's<br>Nutrient Treasure:</h2>
    <div class="copy story">
      <p>Phytoplankton is the foundation of life. It is the first plant in the entire food chain.</p>
      <p>Phytoplankton is a microscopic powerhouse. Your pet's body absorbs billions of phytoplankton with every serving.</p>
      <p>Packed with the building blocks of life, phytoplankton addresses multiple aspects of your pet's health in one simple supplement.</p>
    </div>
    <div class="stripes"><span class="stripe-light"></span><span class="stripe-peach"></span><span class="stripe-red"></span></div>
  </section>

  <div class="print-side">PRINT<br>SIDE</div>

  <section class="panel facts" aria-label="Supplement facts panel">
    <div class="corner-red"></div>
    <div class="facts-table">
      <div class="facts-head">SUPPLEMENT FACTS</div>
      <div class="facts-row row-peach"><span>Serving Size: 1 Scoop/Day<br>Servings per Container: 30</span><span><br>Amount per Serving %DV</span></div>
      <div class="facts-row row-light"><span>Microalgae Nannochloropsis Gaditana &nbsp;500mg</span><span>‡</span></div>
      <div class="facts-row row-pale"><span>‡ Daily value not established.</span></div>
    </div>
    <p class="copy notice">These statements have not been evaluated by the Food and Drug Administration. This product is not intended to diagnose, treat, cure, or prevent any disease.<br><b>Store in a cool, dry place.</b></p>
    <p class="copy distributor">Distributed By:<br><b>Tidewell Pet Nutrition Inc.</b><br>42 Harbour Road,<br>Saint John, New Brunswick<br>Canada E2L 4K9</p>
    <p class="copy warnings">Warnings: Check with a qualified healthcare professional before using this product if you are pregnant, breastfeeding, or taking blood thinners. You should call your doctor for medical advice about serious adverse events. To report a serious adverse event or obtain product information contact: 1 800 555 0147</p>
    <p class="copy care">Customer Care: 1 800 555 0147<br>tidewellpet.example</p>
  </section>

  <section class="panel back" aria-label="Back panel">
    <div class="back-hero"><p>Our premium phytoplankton powder is a extraordinary supplement. It infuses your pet's body with pure, plant-based nutrients and potent antioxidants.</p></div>
    <div class="copy story">
      <p>Phytoplankton goes beyond ordinary supplements; it's a path to optimal health. In just a few weeks, your pet will experience a feeling of calm and strength, the kind of wellness our customers often say they've been seeking.</p>
      <p>Join those who have discovered the transformative power of phytoplankton. See the difference for yourself and understand why it's not just a supplement, but a revolution in pet health and vitality.</p>
    </div>
  </section>

  <div class="lot-line">Exp: 22025/03/Lot No.:12222</div>

  <svg class="cut-lines" viewBox="0 0 692 830" fill="none" stroke="#1a1a1a" stroke-width="1" aria-hidden="true">
    <path d="M45,55 L45,42 Q45,3 85,3 L185,3 Q225,3 225,42 L225,55 Z"/>
    <rect x="45" y="55" width="180" height="145"/>
    <path d="M45,203 L0,207 L0,520 L45,523"/>
    <rect x="45" y="200" width="180" height="325"/>
    <path d="M225,200 L225,102 L350,102 L355,180 L370,192 L370,200"/>
    <rect x="225" y="200" width="145" height="328"/>
    <path d="M225,528 L240,545 L243,625 L370,625 L370,528"/>
    <rect x="370" y="200" width="180" height="328"/>
    <path d="M370,528 L370,670 L550,670 L550,528"/>
    <path d="M370,670 L375,698 Q385,725 420,725 L500,725 Q535,725 545,698 L550,670"/>
    <path d="M550,200 L550,192 L565,180 L570,102 L692,102 L692,200"/>
    <rect x="550" y="200" width="142" height="328"/>
    <path d="M550,528 L550,625 L675,625 L680,545 L692,528"/>
  </svg>

  <div class="swatches" aria-label="Colour palette">
    <div class="swatch swatch-red"></div>
    <div class="swatch swatch-black"></div>
    <div class="swatch swatch-peach"></div>
    <div class="swatch swatch-green"></div>
  </div>
</main>
</body>
</html>
```